Web Design Project

I need designs (PSD only - no programming) for several pages of a new website helping train operators to manage key information about their traindrivers.
The main feature of this website is the management of personnel records (create, edit, search, delete). Another key aspect is the management of user privileges. Since this is a new website we also need a user friendly frontpage, pricing information and how it works sections.
This can be broken down into 9 pages for which we need designs (PSDs).
1. Home
2. Driver record
3. How it works
4. Pricing
5. User administration
6. Help
7. Record list view
8. Login
9. Registration
Navigation (not logged in) are: Home | How it works | Pricing | Customers | About us | Contact
Navigation (logged in) are: Overview | Administration | Manage records | Billing | Help | Contact
Footer: Customer logos | Awards | Terms & Conditions | Privacy
To provide the best support for you to come up with a strong design proposal I will provide DAILY feedback to all participants. We have also created concept mockups (attached) and example pages (below) for each section to give you a clear sense of what we look for.
The core concepts for a successful bid are that the website is EASY to understand, INTUITIVE to navigate, and SIMPLE to use. Most of our users lack technical background and are looking for tool to simplify their work.
The strongest participants (winner and close contenders) will have the opportunity to additional commissioned work on additional sections not included in this brief.
Example Pages (by section)
1. http://www.quorvane.example/site-keepers/
1. http://www.vrm.example/
1. http://www.tovasko.example/
1. http://www.glimmerhootz.example/
2. http://www.pendlo.example/profile_edit.gne
3. https://www.drav.example/how-it-works/
3. http://www.wexalot.example/learn
4. http://www.brindlequay.example/crm/editions-pricing.jsp
4. http://www.quorvane.example/site-keepers/rates
6. https://support.zoltu.example/en-gb/
6. http://help.harbenquill.example/contact_us
8. https://www.morvelnet.example/uas/login
8. https://www.harbenquill.example/login
8. http://www.ublix.example/login/index
For form designs we like Ferrowen, Okvo, Pendlo, Morvelnet, Trellimap and the concepts presented by Dario Fenstermack in his classic Panel Craft Beyond the Checkboxes.
For additional guidance see mockups attached!
Target Market(s)
Security, human resources and admin support employees for train operators.
Industry/Entity Type
Learn
Requirements
Should not have
- Home page should not have
Social media icons (trellimap, pellomb, Morvelnet, RSS feed)
Contact forms
Read more links
Old trains

```html
<!DOCTYPE html>
<html lang="en">
<head>
<meta charset="utf-8">
<title>Railcertra – Home</title>
<link rel="stylesheet" href="https://fonts.googleapis.com/css2?family=Arimo:wght@400;700&display=swap">
<style>
:root{
  --blue:#1e73c8;
  --blue-dark:#0a6aa8;
  --hero-top:#1a8ccc;
  --hero-bottom:#0a70b0;
  --green:#86c51b;
  --green-dark:#5f9a0c;
  --text:#222;
  --body-text:#444;
  --light-bg:#f4f4f4;
  --band-bg:#e9e9e9;
  --line:#d2d2d2;
  --footer-bg:#5a5a5a;
  --logo-grey:#8a8a8a;
}
*{margin:0;padding:0;box-sizing:border-box}
html,body{width:1200px;height:2169px;overflow:hidden}
body{font-family:"Arimo",Arial,sans-serif;color:var(--text);background:var(--light-bg);position:relative}
a{color:inherit;text-decoration:none}
.abs{position:absolute}

/* header */
.site-header{position:absolute;left:0;top:0;width:1200px;height:108px;background:linear-gradient(#fff,#e4e4e4);border-top:3px solid var(--blue)}
.account-tab{left:798px;top:0;width:113px;height:26px;background:var(--blue);border-radius:0 0 14px 14px;color:#fff;font-size:12px;text-align:center;line-height:24px}
.language{left:933px;top:7px;font-size:12px;color:#555;display:flex;gap:12px;align-items:center}
.language .select{width:78px;height:17px;border:1px solid #aab;background:#fff;font-size:11px;padding-left:4px;line-height:15px;position:relative}
.language .select::after{content:"";position:absolute;right:0;top:0;width:14px;height:15px;background:#c8d4e6}
.brand{left:119px;top:38px;font-size:34px;font-weight:700;color:var(--blue)}
.main-nav{left:398px;top:45px;display:flex;font-size:17px;font-weight:700}
.main-nav a{height:30px;line-height:30px}
.main-nav .current{background:var(--blue);color:#fff;border-radius:15px;width:93px;text-align:center}

/* hero */
.hero{left:0;top:108px;width:1200px;height:414px;background:radial-gradient(circle at 78% 10%,#2aa0de 0,var(--hero-top) 35%,var(--hero-bottom) 100%)}
.hero h1{left:119px;top:63px;width:360px;font-size:37px;line-height:43px;color:#fff;font-weight:700}
.hero p{left:119px;top:171px;width:341px;font-size:13.5px;line-height:17px;color:#fff;font-weight:700;text-align:justify}
.btn{position:absolute;height:42px;background:linear-gradient(#9bd42c,var(--green));border-bottom:3px solid var(--green-dark);border-radius:3px;color:#fff;font-weight:700;font-size:21px;text-align:center;line-height:39px}
.hero-photo{left:530px;top:66px;width:389px;height:277px;border:4px solid #fff;background:linear-gradient(160deg,#8e9aa6,#d8dde2 45%,#6b6f74);box-shadow:0 2px 6px rgba(0,0,0,.3)}
.hero-cert{left:806px;top:193px;width:274px;height:304px;height:196px;border:3px solid #111;background:linear-gradient(#fbfbf6,#ecece4)}

/* features */
.features{left:0;top:522px;width:1200px;height:377px;background:#f2f2f2}
.feature{position:absolute;width:330px}
.feature svg{position:absolute;left:0;top:-6px}
.feature h3{position:absolute;left:75px;top:0;font-size:18px;font-weight:400;color:#222}
.feature p{position:absolute;left:75px;top:28px;width:217px;font-size:12.5px;line-height:14px;color:#444;text-align:justify}

/* call to action band */
.cta-band{left:0;top:899px;width:1200px;height:88px;background:var(--band-bg);border-top:1px solid var(--line);border-bottom:1px solid var(--line)}
.cta-band p{left:119px;top:21px;width:600px;font-size:18px;line-height:22px;color:#444}

/* how it works */
.section-title{left:119px;top:1024px;font-size:23px;font-weight:400;color:#222}
.step-art{position:absolute}
.step-num{position:absolute;width:74px;height:74px;border-radius:50%;background:radial-gradient(circle at 40% 35%,#6a6a6a,#2e2e2e);border:3px solid #d8d8d8;box-shadow:0 0 0 1px #999;color:#fff;font-size:40px;font-weight:700;text-align:center;line-height:68px}
.step h2{position:absolute;font-size:23px;font-weight:700;color:var(--blue)}
.step p{position:absolute;width:410px;font-size:13.5px;line-height:19px;color:#444;text-align:justify}

/* partners & footer */
.partners-line{left:0;top:1953px;width:1200px;height:1px;background:var(--line)}
.partners-band{left:0;top:1954px;width:1200px;height:185px;background:#fff}
.partner{position:absolute;background:#b5b5b5}
.train-band{left:0;top:2050px;width:1200px;height:89px;background:linear-gradient(#fff,#d2d2d2)}
.site-footer{left:0;top:2139px;width:1200px;height:30px;background:var(--footer-bg);color:#fff;font-size:11.5px;line-height:30px}
.site-footer .copy{position:absolute;left:119px}
.site-footer .links{position:absolute;right:120px}
</style>
</head>
<body>

<header class="site-header">
  <div class="abs account-tab"><a href="#">Sign up</a> &nbsp;|&nbsp; <a href="#">Login</a></div>
  <div class="abs language">Language <span class="select">English</span></div>
  <div class="abs brand">Railcertra</div>
  <nav class="abs main-nav">
    <a class="current" href="#">Home</a>
    <a href="#" style="margin-left:22px">How it works</a>
    <a href="#" style="margin-left:42px">Pricing</a>
    <a href="#" style="margin-left:36px">Customers</a>
    <a href="#" style="margin-left:37px">About us</a>
    <a href="#" style="margin-left:40px">Contact</a>
  </nav>
</header>

<section class="abs hero">
  <h1 class="abs">Lorem ipsum dolor sit amet</h1>
  <p class="abs">Lorem ipsum dolor sit amet, consectetur adipiscing elit. Curabitur metus nisl, scelerisque eu venenatis at, blandit commodo diam. Nulla facilisi. Ut eu orci eros, in volutpat lectus. Vestibulum at nunc urna, nec gravida mi. Fusce metus velit, semper nec viverra non, pharetra ut ipsum.</p>
  <a class="btn" href="#" style="left:119px;top:312px;width:155px">Sign up</a>
  <a class="btn" href="#" style="left:307px;top:312px;width:153px">Buy Now</a>
  <div class="abs hero-photo" role="img" aria-label="Photo of a modern high-speed train at a station platform"></div>
  <div class="abs hero-cert" role="img" aria-label="Good driver certificate of appreciation with a seal"></div>
</section>

<section class="abs features">
  <div class="feature" style="left:119px;top:47px">
    <svg width="64" height="56" viewBox="0 0 64 56"><path d="M32 4 2 30h9v24h16V38h10v16h16V30h9z" fill="var(--blue)"/></svg>
    <h3>About Railcertra</h3>
    <p>Lorem ipsum dolor sit amet, consectetur adipisicing elit, sed do eiusmod tempor incididunt ut labore dolore magna aliqua. Ut enim ad minim veniam, quis nostrud exercitation ullamco.</p>
  </div>
  <div class="feature" style="left:460px;top:47px">
    <svg width="60" height="56" viewBox="0 0 60 56"><g fill="none" stroke="var(--blue)" stroke-width="7"><path d="M22 10l-12 20"/><path d="M40 10l12 20"/><path d="M10 44h40"/></g><g fill="var(--blue)"><path d="M28 4l8 10H22z"/><path d="M54 40l-2 12-10-6z"/><path d="M4 38l12 0-6 12z"/></g></svg>
    <h3>Main Features</h3>
    <p>Lorem ipsum dolor sit amet, consectetur adipisicing elit, sed do eiusmod tempor incididunt ut labore dolore magna aliqua. Ut enim ad minim veniam, quis nostrud exercitation ullamco.</p>
  </div>
  <div class="feature" style="left:794px;top:47px">
    <svg width="56" height="56" viewBox="0 0 56 56"><path d="M28 2l8 18 18 2-14 12 4 19-16-10-16 10 4-19L2 22l18-2z" fill="var(--blue)"/></svg>
    <h3>Easy to use</h3>
    <p>Lorem ipsum dolor sit amet, consectetur adipisicing elit, sed do eiusmod tempor incididunt ut labore dolore magna aliqua. Ut enim ad minim veniam, quis nostrud exercitation ullamco.</p>
  </div>
  <div class="feature" style="left:119px;top:208px">
    <svg width="60" height="62" viewBox="0 0 60 62"><path d="M4 4h52v30c0 14-26 26-26 26S4 48 4 34z" fill="var(--blue)"/><path d="M16 32l10 10 18-20" stroke="#fff" stroke-width="6" fill="none"/></svg>
    <h3>Cost Effective</h3>
    <p>Lorem ipsum dolor sit amet, consectetur adipisicing elit, sed do eiusmod tempor incididunt ut labore dolore magna aliqua. Ut enim ad minim veniam, quis nostrud exercitation ullamco.</p>
  </div>
  <div class="feature" style="left:460px;top:208px">
    <svg width="56" height="60" viewBox="0 0 56 60"><rect x="12" y="2" width="40" height="54" rx="4" fill="none" stroke="var(--blue)" stroke-width="5"/><path d="M20 18h24M20 28h24M20 38h24" stroke="var(--blue)" stroke-width="4"/><rect x="2" y="10" width="10" height="40" rx="3" fill="var(--blue)"/></svg>
    <h3>Documentation</h3>
    <p>Lorem ipsum dolor sit amet, consectetur adipisicing elit, sed do eiusmod tempor incididunt ut labore dolore magna aliqua. Ut enim ad minim veniam, quis nostrud exercitation ullamco.</p>
  </div>
  <div class="feature" style="left:794px;top:208px">
    <svg width="60" height="60" viewBox="0 0 60 60"><g fill="none" stroke="var(--blue)" stroke-width="3"><ellipse cx="30" cy="30" rx="27" ry="10"/><ellipse cx="30" cy="30" rx="27" ry="10" transform="rotate(60 30 30)"/><ellipse cx="30" cy="30" rx="27" ry="10" transform="rotate(-60 30 30)"/></g><circle cx="30" cy="30" r="5" fill="var(--blue)"/></svg>
    <h3>Admin Preferences</h3>
    <p>Lorem ipsum dolor sit amet, consectetur adipisicing elit, sed do eiusmod tempor incididunt ut labore dolore magna aliqua. Ut enim ad minim veniam, quis nostrud exercitation ullamco.</p>
  </div>
</section>

<section class="abs cta-band">
  <p class="abs">Lorem ipsum dolor sit amet, consectetur adipisicing elit, sed do eiusmod tempor incididunt ut labore dolore magna aliqua.</p>
  <a class="btn" href="#" style="left:738px;top:21px;width:155px">Sign up</a>
  <a class="btn" href="#" style="left:925px;top:21px;width:155px">Buy Now</a>
</section>

<h2 class="abs section-title">How It Works</h2>

<div class="step">
  <div class="step-art" role="img" aria-label="Cartoon train conductor holding a signal horn" style="left:217px;top:1085px;width:209px;height:271px;background:radial-gradient(circle at 50% 58%,#4b8fd0 0,#3c6fb0 40%,#f4f4f4 42%)"></div>
  <div class="step-num" style="left:561px;top:1160px">1</div>
  <h2 style="left:671px;top:1130px">Register train driver information</h2>
  <p style="left:671px;top:1168px">Lorem ipsum dolor sit amet, consectetur adipiscing elit. Donec sagittis congue enim, eget luctus tellus luctus ac. Vestibulum mattis vehicula mi ut vestibulum. Quisque nulla nisi, dictum in tristique id, tincidunt at sapien. Maecenas a rhoncus dolor. Fusce felis massa, tempus quis ullamcorper.</p>
</div>

<div class="step">
  <h2 style="left:119px;top:1424px">Update records as data change</h2>
  <p style="left:119px;top:1461px">Lorem ipsum dolor sit amet, consectetur adipiscing elit. Donec sagittis congue enim, eget luctus tellus luctus ac. Vestibulum mattis vehicula mi ut vestibulum. Quisque nulla nisi, dictum in tristique id, tincidunt at sapien. Maecenas a rhoncus dolor. Fusce felis massa, tempus quis ullamcorper.</p>
  <div class="step-num" style="left:561px;top:1474px">2</div>
  <div class="step-art" role="img" aria-label="Stack of documents with a green upload arrow" style="left:713px;top:1361px;width:273px;height:251px;background:radial-gradient(circle at 30% 72%,#6cc02a 0,#3f8f16 22%,transparent 23%),linear-gradient(#eef1f3,#cfd7db)"></div>
</div>

<div class="step">
  <div class="step-art" role="img" aria-label="Certificate with a rosette and a green alarm clock" style="left:212px;top:1640px;width:303px;height:260px;background:radial-gradient(circle at 70% 65%,#7bc62e 0,#4c9a1a 24%,transparent 25%),linear-gradient(#eef3f8,#d6e0ea)"></div>
  <div class="step-num" style="left:561px;top:1749px">3</div>
  <h2 style="left:671px;top:1704px">Certificate is automatically ready</h2>
  <p style="left:671px;top:1742px">Lorem ipsum dolor sit amet, consectetur adipiscing elit. Donec sagittis congue enim, eget luctus tellus luctus ac. Vestibulum mattis vehicula mi ut vestibulum. Quisque nulla nisi, dictum in tristique id, tincidunt at sapien. Maecenas a rhoncus dolor. Fusce felis massa, tempus quis ullamcorper.</p>
</div>

<div class="abs partners-line"></div>
<section class="abs partners-band" aria-label="Customer logos">
  <div class="partner" style="left:128px;top:42px;width:64px;height:26px;border-radius:2px"></div>
  <div class="partner" style="left:244px;top:44px;width:92px;height:22px;border-radius:2px"></div>
  <div class="partner" style="left:397px;top:40px;width:70px;height:30px;border-radius:2px"></div>
  <div class="partner" style="left:530px;top:43px;width:112px;height:24px;border-radius:2px"></div>
  <div class="partner" style="left:700px;top:36px;width:44px;height:40px;border-radius:3px"></div>
  <div class="partner" style="left:802px;top:33px;width:48px;height:48px;border-radius:50%"></div>
  <div class="partner" style="left:910px;top:40px;width:52px;height:32px;border-radius:50%"></div>
  <div class="partner" style="left:1008px;top:38px;width:68px;height:32px;border-radius:2px"></div>
</section>
<div class="abs train-band" role="img" aria-label="Faint grey silhouette of a high-speed train"></div>

<footer class="abs site-footer">
  <span class="copy">Copyright © 2012 Railcertra. All Rights Reserved | Terms &amp; Conditions</span>
  <span class="links">Home | How it works | Pricing | Customers | About us | Contact</span>
</footer>

</body>
</html>
```